TRV Mechanical Solutions Business Card Design

Business card design

Thinking just large logo on one side with a phone number and the back side is contact info with services we offer with a industrial plant across the bottom of the card

See must haves. I will be laser etching these business cards on black metal business cards as well as full color card stock. So must be bold and professional.

Target Market(s)

Industrial manufacturing

Contact Information for Business Card

Industrial manufacturing construction business specializing in consulting project managment and completing projects turn key

Font styles to use
Other font styles liked:
• See Logo for colors and font style

Requirements
Must have
• TRV Mechanical Solutions
• Gerald Munroe
• 2847 Alderwick Lane
• Bel Air, MD, 21047
• Project Managment
• Consulting
• Turn Key Industrial Projects
• I’d like a industrial manufacturing “cityline” on the back side bottom of the
• I’d like to be able to print these business cards in regular color on card stock but I’d also like the design to be etched into black metal business cards

```html
<!DOCTYPE html>
<html lang="en">
<head>
<meta charset="utf-8">
<title>TRV Mechanical Solutions – Business Cards</title>
<link rel="stylesheet" href="https://fonts.googleapis.com/css2?family=Roboto:wght@400;500&display=swap">
<style>
  :root {
    --backdrop: #3a342d;
    --card-black: #161616;
    --brand-blue: #3b62b8;
    --rule-grey: #4a4a4a;
    --muted-grey: #6a6a6a;
    --ink-dark: #141821;
    --ink-mid: #1c2233;
    --ink-light: #e2e7f3;
    --band-rule: #6d8ad0;
    --icon-grey: #6e6e6e;
  }
  * { margin: 0; padding: 0; box-sizing: border-box; }
  html, body {
    width: 1200px; height: 1200px; overflow: hidden;
    background: var(--backdrop);
    font-family: "Roboto", Arial, sans-serif;
  }
  .canvas { position: relative; width: 1200px; height: 1200px; }

  .card {
    position: absolute; left: 240px; width: 720px; height: 410px;
    background: var(--card-black);
    box-shadow: 0 10px 28px rgba(0,0,0,0.45);
    overflow: hidden;
  }
  .card--front { top: 144px; }
  .card--back  { top: 598px; }

  /* Front */
  .front-brand {
    position: absolute; left: 0; right: 0; top: 186px;
    text-align: center;
    font-size: 46px; font-weight: 500; letter-spacing: 1px;
    color: var(--brand-blue);
  }
  .front-phone {
    position: absolute; left: 0; right: 0; top: 318px;
    display: flex; justify-content: center; align-items: center; gap: 10px;
    font-size: 25px; color: var(--brand-blue);
  }
  .front-phone svg { width: 30px; height: 30px; }

  /* Back */
  .back-brand {
    position: absolute; left: 0; right: 0; top: 102px;
    text-align: center;
    font-size: 32px; font-weight: 500; letter-spacing: 1px;
    color: var(--brand-blue);
  }
  .back-address {
    position: absolute; left: 0; right: 0; top: 180px;
    text-align: center; font-size: 17px; letter-spacing: 0.5px;
    color: var(--muted-grey);
  }
  .back-divider {
    position: absolute; left: 0; right: 0; top: 222px; height: 5px;
    background: var(--rule-grey);
  }
  .info-band {
    position: absolute; left: 0; right: 0; top: 227px; bottom: 0;
    background: var(--brand-blue);
  }
  .person { position: absolute; left: 72px; top: 32px; }
  .person__name { font-size: 26px; font-weight: 500; color: var(--ink-dark); }
  .person__role { font-size: 17px; line-height: 21px; color: var(--ink-mid); margin-top: 4px; }

  .contact-list {
    position: absolute; left: 432px; top: 34px; list-style: none;
    font-size: 16.5px; color: var(--ink-light);
  }
  .contact-list li { display: flex; align-items: center; gap: 9px; height: 24px; }
  .contact-list svg { width: 13px; height: 13px; flex: none; }

  .services {
    position: absolute; left: 60px; right: 60px; top: 126px;
    border-top: 1px solid var(--band-rule);
    padding-top: 12px; text-align: center;
    font-size: 17px; color: var(--ink-light); word-spacing: 2px;
  }
</style>
</head>
<body>
<main class="canvas">

  <section class="card card--front">
    <div class="front-brand">TRV Mechanical Solutions</div>
    <div class="front-phone">
      <svg viewBox="0 0 30 30" aria-hidden="true">
        <circle cx="15" cy="15" r="13" fill="none" stroke="var(--icon-grey)" stroke-width="2"/>
        <path d="M10 9c1-1 2-1 2.5 0l1.5 2.5c.4.8 0 1.5-.7 2l-.8.6c.8 1.8 2 3 3.8 3.8l.6-.8c.5-.7 1.2-1.1 2-.7L21.4 18c1 .5 1 1.5 0 2.5-1.5 1.5-4 1.3-7-1.3-3-2.8-5.8-6.3-4.4-10.2z" fill="var(--icon-grey)"/>
      </svg>
      <span>410 555 0182</span>
    </div>
  </section>

  <section class="card card--back">
    <div class="back-brand">TRV Mechanical Solutions</div>
    <div class="back-address">2847 Alderwick Lane, Bel Air, MD, 21047</div>
    <div class="back-divider"></div>

    <div class="info-band">
      <div class="person">
        <div class="person__name">Gerald Munroe</div>
        <div class="person__role">Founder &amp; CEO<br>TRV Mechanical Solutions</div>
      </div>

      <ul class="contact-list">
        <li>
          <svg viewBox="0 0 13 13" aria-hidden="true"><rect x="3" y="0.5" width="7" height="12" rx="1.2" fill="none" stroke="var(--ink-light)" stroke-width="1.3"/><rect x="5.5" y="10" width="2" height="1" fill="var(--ink-light)"/></svg>
          <span>410 555 0147</span>
        </li>
        <li>
          <svg viewBox="0 0 13 13" aria-hidden="true"><rect x="1" y="3" width="11" height="8" rx="1" fill="var(--ink-light)"/><path d="M1.5 3.5l5 4 5-4" fill="none" stroke="var(--brand-blue)" stroke-width="1"/></svg>
          <span>gmunroe@trvmech.com</span>
        </li>
        <li>
          <svg viewBox="0 0 13 13" aria-hidden="true"><circle cx="6.5" cy="6.5" r="5.5" fill="none" stroke="var(--ink-light)" stroke-width="1.2"/><ellipse cx="6.5" cy="6.5" rx="2.4" ry="5.5" fill="none" stroke="var(--ink-light)" stroke-width="1"/><line x1="1" y1="6.5" x2="12" y2="6.5" stroke="var(--ink-light)" stroke-width="1"/></svg>
          <span>www.trvmech.com</span>
        </li>
      </ul>

      <div class="services">Project Managment &nbsp;|&nbsp; Consulting &nbsp;|&nbsp; Turn Key Industrial Projects</div>
    </div>
  </section>

</main>
</body>
</html>
```